Design a leading edge business card for an architectural company

We believe that Velistra Design Collective is redefining the architectural industry. With that, we need a leading edge business card for the company that focuses on landscape architecture, design, and construction.

Our clients are businesses and homeowners so we need a clean, simple, and professional-looking logo. But we want something special. Design must be elegant but unexpected.

Color preferences:
- Preferably with black background but not a must
- Text should be light colored
- Overall, don’t use too much colors.

Content:
- Front of card must contain either just the logo or the logo and business name only.
- Back of card will show the other information (name, title, phone number, email, website, location).

Style:
- Maybe embossing, de-bossing, or spot UV
- Layout should be landscape unless you prove us otherwise.

Size: 1050 x 600 pixels (with 1/8th inch bleed: 1125 x 675 pixels)

Attached is the company logo to incorporate in the design.

```html
<!DOCTYPE html>
<html lang="en">
<head>
<meta charset="utf-8">
<title>Velistra Design Collective — Business Card</title>
<link rel="stylesheet" href="https://fonts.googleapis.com/css2?family=Cinzel:wght@400&family=Open+Sans:wght@300;400&display=swap">
<style>
  :root {
    --page: #e9e7e4;
    --card-black: #0d0b0b;
    --card-black-soft: #1c1919;
    --gloss: rgba(255,255,255,0.06);
    --bar-white: #ffffff;
    --text-light: #f4f4f4;
    --text-muted: #a9a9a9;
    --rule: #8a8a8a;
  }
  * { margin: 0; padding: 0; box-sizing: border-box; }
  html, body { width: 1200px; height: 912px; overflow: hidden; background: var(--page); }
  .canvas {
    width: 1200px; height: 912px;
    display: flex; flex-direction: column; align-items: center; justify-content: center;
    gap: 24px;
  }
  .card {
    position: relative;
    width: 700px; height: 400px;
    background: linear-gradient(120deg, var(--card-black) 0%, var(--card-black-soft) 45%, var(--card-black) 100%);
    overflow: hidden;
    box-shadow: 0 8px 24px rgba(0,0,0,0.25);
    font-family: "Open Sans", sans-serif;
    color: var(--text-light);
  }
  .card::after {
    content: ""; position: absolute; inset: 0;
    background: linear-gradient(100deg, transparent 38%, var(--gloss) 48%, transparent 60%);
    pointer-events: none;
  }
  .card__bar {
    position: absolute; top: 0; height: 22px; background: var(--bar-white);
  }
  .card--front .card__bar { left: 0; width: 300px; }
  .card--back .card__bar { left: 120px; width: 330px; }

  .brand {
    display: flex; flex-direction: column; align-items: center; gap: 10px;
    text-align: center;
  }
  .brand__mark {
    width: 34px; height: 34px; border-radius: 50%;
    border: 2px solid var(--text-light);
  }
  .brand__name {
    font-family: "Cinzel", serif; font-weight: 400;
    font-size: 20px; letter-spacing: 5px; line-height: 1.35;
    color: var(--text-light); text-transform: uppercase;
  }
  .card--front .brand {
    position: absolute; left: 50%; top: 50%; transform: translate(-50%, -50%);
  }
  .card--front .brand__name { font-size: 24px; }
  .card__web {
    position: absolute; right: 110px; bottom: 34px;
    font-size: 13px; letter-spacing: 0.3px; color: var(--text-light);
  }

  .card--back .brand {
    position: absolute; left: 50px; top: 50%; transform: translateY(-50%);
    width: 250px;
  }
  .card--back .brand__name { font-size: 18px; }
  .card__divider {
    position: absolute; left: 340px; top: 90px; width: 1px; height: 220px;
    background: var(--rule);
  }
  .contact {
    position: absolute; left: 365px; top: 110px;
  }
  .contact__name { font-size: 30px; font-weight: 400; line-height: 1.1; }
  .contact__title {
    font-size: 15px; font-weight: 300; color: var(--text-muted);
    letter-spacing: 1.5px; margin-bottom: 26px;
  }
  .contact__list { list-style: none; }
  .contact__item {
    display: flex; align-items: center; gap: 8px;
    font-size: 13px; line-height: 21px;
  }
  .contact__icon { width: 13px; height: 13px; flex: none; }
</style>
</head>
<body>
<main class="canvas">

  <section class="card card--front" aria-label="Card front">
    <div class="card__bar"></div>
    <div class="brand">
      <span class="brand__mark"></span>
      <span class="brand__name">Velistra<br>Design Collective</span>
    </div>
    <p class="card__web">www.company.com</p>
  </section>

  <section class="card card--back" aria-label="Card back">
    <div class="card__bar"></div>
    <div class="brand">
      <span class="brand__mark"></span>
      <span class="brand__name">Velistra<br>Design Collective</span>
    </div>
    <div class="card__divider"></div>
    <div class="contact">
      <h1 class="contact__name">Your Name</h1>
      <p class="contact__title">General Manegar</p>
      <ul class="contact__list">
        <li class="contact__item">
          <svg class="contact__icon" viewBox="0 0 16 16"><path d="M8 2 1 8h2v6h4v-4h2v4h4V8h2z" fill="#f4f4f4"/></svg>
          Street Number , Area , City
        </li>
        <li class="contact__item">
          <svg class="contact__icon" viewBox="0 0 16 16"><circle cx="8" cy="8" r="8" fill="#f4f4f4"/><path d="M5 4h2l1 2-1 1c.5 1 1.5 2 2 2l1-1 2 1v2c-4 0-7-3-7-7z" fill="#0d0b0b"/></svg>
          0004015550192
        </li>
        <li class="contact__item">
          <svg class="contact__icon" viewBox="0 0 16 16"><circle cx="8" cy="8" r="8" fill="#f4f4f4"/><rect x="4" y="5" width="8" height="6" fill="none" stroke="#0d0b0b" stroke-width="1.2"/><path d="M4 5l4 3 4-3" fill="none" stroke="#0d0b0b" stroke-width="1.2"/></svg>
          Name@Company.com
        </li>
        <li class="contact__item">
          <svg class="contact__icon" viewBox="0 0 16 16"><circle cx="8" cy="8" r="8" fill="#f4f4f4"/><circle cx="8" cy="8" r="4.5" fill="none" stroke="#0d0b0b" stroke-width="1.2"/><path d="M3.5 8h9M8 3.5v9" stroke="#0d0b0b" stroke-width="1"/></svg>
          Company.com
        </li>
      </ul>
    </div>
  </section>

</main>
</body>
</html>
```